A4 Flier to send to Schools about Manners for School Students

We are expanding and now working with corporate clients as well as teaching etiquette and manners to High School students. This is a the flier we need created. The clients are Assistant Principals and Heads of School so we need to appear professional, approachable and aspirational and fun.
Here is the content and some images that may be useful to get started.

Target Market(s)

Assistant Principals and School Heads

Industry/Entity Type

School

Font styles to use
Sans Serif

Colors
00a990
ffffff

Requirements
Must have
• Cool pictures of young people - pref a mix of Asians, caucasians. Well dressed and happy teens and positive images.
• Logo
• Some use of green and white as this is our corporate style.
• Image of Clara Pendry
• Image of Ingrid Dowlatte
Nice to have
• I have put it all in the flier I have attached so please come back to me with any questions.
Should not have
• Any teens of African descent - only as Australian is mostly caucasian and Asian.
• Pinks

```html
<!DOCTYPE html>
<html lang="en">
<head>
<meta charset="utf-8">
<title>Etiquette and Manners for Students – Flier</title>
<link rel="stylesheet" href="https://fonts.googleapis.com/css2?family=Montserrat:wght@600;700;800&family=Open+Sans:wght@400;600;700&display=swap">
<style>
  :root {
    --teal: #00a990;
    --teal-dark: #00806d;
    --teal-soft: #d9f2ee;
    --ink: #1f2a2c;
    --ink-soft: #3c4a4c;
    --white: #ffffff;
    --paper: #ffffff;
    --sky: #bfe6f2;
  }
  * { box-sizing: border-box; margin: 0; padding: 0; }
  html, body { width: 870px; height: 1200px; overflow: hidden; background: var(--paper); }
  body { font-family: "Open Sans", Arial, sans-serif; color: var(--ink); }

  .flier { position: relative; width: 870px; height: 1200px; background: var(--paper); }

  .brand { position: absolute; top: 24px; left: 0; width: 100%; display: flex; justify-content: center; align-items: center; gap: 12px; }
  .brand-dot { width: 16px; height: 16px; border-radius: 50%; background: var(--teal); }
  .brand-name { font-family: "Montserrat", Arial, sans-serif; font-weight: 700; font-size: 24px; color: var(--teal); letter-spacing: 0.5px; }

  .headline { position: absolute; top: 84px; left: 0; width: 100%; text-align: center; font-family: "Montserrat", Arial, sans-serif; font-weight: 800; color: var(--teal); line-height: 1.05; }
  .headline .line-1 { font-size: 44px; display: block; }
  .headline .line-2 { font-size: 40px; display: block; }

  .intro { position: absolute; top: 192px; left: 70px; width: 730px; text-align: center; }
  .intro-question { font-weight: 700; font-size: 17px; line-height: 1.3; margin-bottom: 6px; }
  .intro-body { font-size: 14px; line-height: 1.4; color: var(--ink-soft); }

  .topics-band { position: absolute; top: 318px; left: 0; width: 100%; height: 224px; background: var(--teal); }
  .topics-card { position: absolute; top: 14px; left: 36px; width: 470px; height: 196px; background: var(--white); display: flex; padding: 10px; gap: 12px; overflow: hidden; }
  .topics-photo { flex: 0 0 140px; height: 176px; background: linear-gradient(160deg, #8fc7e0, #e8d8b6 70%, #c69a6a); }
  .topics-list { flex: 1 1 auto; min-width: 0; }
  .topics-list h2 { font-family: "Montserrat", Arial, sans-serif; font-weight: 800; color: var(--teal); font-size: 19px; line-height: 1.1; margin-bottom: 4px; }
  .topics-list ul { list-style: none; font-size: 10.5px; line-height: 1.3; font-weight: 600; }
  .topics-list li::before { content: "• "; color: var(--teal); }
  .topics-art { position: absolute; top: 14px; right: 36px; width: 290px; height: 196px; background: linear-gradient(135deg, var(--sky), #f4f9fb 55%, #cfe9d9); }

  .respect { position: absolute; top: 564px; width: 112px; height: 112px; border-radius: 50%; background: var(--teal); color: var(--white); display: flex; align-items: center; justify-content: center; text-align: center; font-family: "Montserrat", Arial, sans-serif; font-weight: 800; font-size: 19px; line-height: 1.1; }
  .respect--give { left: 36px; }
  .respect--earn { right: 36px; }

  .agenda-head { position: absolute; top: 568px; left: 160px; width: 550px; text-align: center; }
  .agenda-head h2 { font-family: "Montserrat", Arial, sans-serif; font-weight: 800; color: var(--teal); font-size: 32px; line-height: 1.15; }
  .agenda-head .agenda-intro { font-weight: 600; font-size: 17px; margin: 6px 0 4px; }
  .agenda-head .agenda-question { font-weight: 700; font-size: 19px; line-height: 1.3; }

  .agenda-cols { position: absolute; top: 708px; left: 36px; width: 798px; display: flex; justify-content: space-between; }
  .agenda-col { width: 380px; font-size: 14px; line-height: 1.45; }
  .agenda-col h3 { font-size: 14px; font-weight: 700; }
  .agenda-col p + h3 { margin-top: 10px; }

  .pricing { position: absolute; top: 940px; left: 36px; width: 440px; }
  .pricing-label { font-family: "Montserrat", Arial, sans-serif; font-weight: 700; color: var(--teal); font-size: 26px; }
  .pricing-row { display: flex; align-items: center; gap: 14px; margin-top: 4px; }
  .price { font-family: "Montserrat", Arial, sans-serif; font-weight: 800; color: var(--teal); line-height: 1; flex: 0 0 auto; }
  .price-amount { font-size: 60px; display: block; }
  .price-term { font-size: 20px; font-weight: 700; color: var(--ink); display: block; margin-top: 4px; }
  .price-to { flex: 0 0 50px; width: 50px; height: 50px; border-radius: 50%; background: var(--teal); color: var(--white); display: flex; align-items: center; justify-content: center; font-family: "Montserrat", Arial, sans-serif; font-weight: 700; font-size: 18px; }

  .included { position: absolute; top: 964px; left: 496px; width: 338px; font-size: 14px; line-height: 1.5; }
  .included h3 { font-size: 15px; font-weight: 700; margin-bottom: 2px; }
  .included ul { padding-left: 18px; }

  .footer-rule { position: absolute; bottom: 0; left: 0; width: 100%; height: 26px; background: var(--teal); }
  .footer-rule-thin { position: absolute; bottom: 34px; left: 0; width: 100%; height: 4px; background: var(--teal-soft); }
</style>
</head>
<body>
<main class="flier">
  <header class="brand">
    <span class="brand-dot"></span>
    <span class="brand-name">The Fine Conduct Company</span>
  </header>

  <h1 class="headline">
    <span class="line-1">ETIQUETTE AND MANNERS</span>
    <span class="line-2">FOR STUDENTS</span>
  </h1>

  <section class="intro">
    <p class="intro-question">Are you frustrated by the lack of manners and courtesy shown by students today?</p>
    <p class="intro-body">Reports show that students are applying for jobs lacking social skills and etiquette, making them unprepared for part time jobs and full time workplaces. The sooner they learn good habits around manners and etiquette, the more well-rounded and prepared they will be for leadership opportunities, employment and forming good relationships.</p>
  </section>

  <section class="topics-band">
    <div class="topics-card">
      <div class="topics-photo" role="img" aria-label="Photo of a smiling, well dressed student"></div>
      <div class="topics-list">
        <h2>TOPICS</h2>
        <ul>
          <li>Modern manners for young people</li>
          <li>How to introduce and others yourself correctly</li>
          <li>Job Interview Preparation</li>
          <li>Formal Preparation</li>
          <li>Netiquette, conduct with mobiles, devices and social media</li>
          <li>Table Manners</li>
          <li>Deportment, how to walk, sit, carry yourself with poise and confidence</li>
          <li>Dating Etiquette</li>
        </ul>
      </div>
    </div>
    <div class="topics-art" role="img" aria-label="Illustration of social media speech bubbles and a smartphone"></div>
  </section>

  <div class="respect respect--give">GIVE<br>RESPECT</div>
  <div class="respect respect--earn">EARN<br>RESPECT</div>

  <section class="agenda-head">
    <h2>SAMPLE ONE HOUR AGENDA</h2>
    <p class="agenda-intro">Introduction</p>
    <p class="agenda-question">What are good vs bad manners?<br>Why is it important today?</p>
  </section>

  <section class="agenda-cols">
    <div class="agenda-col">
      <h3>The Rules</h3>
      <p>Appropriate conduct for young ladies and gentlemen</p>
      <h3>The First Impression</h3>
      <p>How to make a good first impression<br>Speaking clearly<br>What to wear, where and when,<br>dressing appropriate for the occasion<br>What not to wear, where and when incl job interviews</p>
    </div>
    <div class="agenda-col">
      <h3>Introductions</h3>
      <p>How to introduce yourself correctly<br>How to introduce one person to another<br>Handshaking skills<br>Putting it all together<br>Role plays</p>
    </div>
  </section>

  <section class="pricing">
    <p class="pricing-label">Prices from</p>
    <div class="pricing-row">
      <div class="price"><span class="price-amount">$500</span><span class="price-term">for 1 hour</span></div>
      <div class="price-to">to</div>
      <div class="price"><span class="price-amount">$1500</span><span class="price-term">for day</span></div>
    </div>
  </section>

  <section class="included">
    <h3>What's included:</h3>
    <ul>
      <li>handout to take home to parents</li>
      <li>classroom poster</li>
      <li>copy of “Polished Habits” book for School</li>
    </ul>
  </section>

  <div class="footer-rule-thin"></div>
  <div class="footer-rule"></div>
</main>
</body>
</html>
```